Business Card Design

I would like a new business card design for an accounting firm that specializes in resolving clients tax problems. I want the card to give the impression that we are not your typical stodgy accounting firm, but at the same time we will get the job done.
Industry/Entity Type
Business
Contact Information for Business Card
Marcus T Kelbeck
Certified Public Accountant
27-08 63rd Avenue
Sunnyside, NY 11104
Tel: (718) 555-0143
Fax: (888) 555-0176
e-mail: mtkledger@quillpost.net
website: harborstonefiscalaidgroup.com

```html
<!DOCTYPE html>
<html lang="en">
<head>
<meta charset="UTF-8">
<title>Marcus T Kelbeck – Business Card</title>
<link href="https://fonts.googleapis.com/css2?family=Open+Sans:wght@400;700&display=swap" rel="stylesheet">
<style>
  :root {
    --backdrop: #2a2c30;
    --card: #ffffff;
    --navy: #0f3a78;
    --ink: #1b1b1b;
    --muted: #4a4a4a;
  }
  * { margin: 0; padding: 0; box-sizing: border-box; }
  html, body {
    width: 1200px;
    height: 864px;
    overflow: hidden;
    background: var(--backdrop);
    font-family: "Open Sans", Arial, sans-serif;
  }
  .stage {
    position: relative;
    width: 1200px;
    height: 864px;
  }
  .card {
    position: absolute;
    top: 277px;
    width: 540px;
    height: 309px;
    background: var(--card);
    border-radius: 3px;
  }
  .card--front { left: 40px; }
  .card--back { left: 620px; }

  .brand {
    display: flex;
    align-items: center;
    gap: 10px;
  }
  .brand__mark {
    width: 16px;
    height: 16px;
    background: var(--navy);
  }
  .brand__name {
    font-weight: 700;
    color: var(--navy);
    letter-spacing: 0.04em;
    text-transform: uppercase;
    white-space: nowrap;
  }
  .card--front .brand {
    position: absolute;
    left: 50%;
    top: 50%;
    transform: translate(-50%, -50%);
  }
  .card--front .brand__name { font-size: 30px; }
  .card--front .brand__mark { width: 22px; height: 22px; }

  .card--back .brand {
    position: absolute;
    left: 34px;
    top: 30px;
  }
  .card--back .brand__name { font-size: 20px; }

  .title {
    position: absolute;
    left: 34px;
    top: 62px;
    font-size: 11px;
    letter-spacing: 0.12em;
    text-transform: uppercase;
    color: var(--muted);
  }
  .address {
    position: absolute;
    left: 34px;
    top: 132px;
    font-size: 14px;
    line-height: 19px;
    color: var(--ink);
    font-style: normal;
  }
  .contacts {
    position: absolute;
    left: 34px;
    top: 182px;
    list-style: none;
    font-size: 14px;
    color: var(--ink);
  }
  .contacts li {
    display: flex;
    align-items: center;
    gap: 8px;
    height: 22px;
  }
  .contacts svg {
    width: 12px;
    height: 12px;
    fill: var(--navy);
    flex: none;
  }
</style>
</head>
<body>
<main class="stage">
  <section class="card card--front" aria-label="Card front">
    <div class="brand">
      <span class="brand__mark"></span>
      <span class="brand__name">Marcus T Kelbeck</span>
    </div>
  </section>

  <section class="card card--back" aria-label="Card back">
    <div class="brand">
      <span class="brand__mark"></span>
      <span class="brand__name">Marcus T Kelbeck</span>
    </div>
    <p class="title">Certified Public Accountant</p>
    <address class="address">27-08 63rd Avenue<br>Sunnyside, NY 11104</address>
    <ul class="contacts">
      <li>
        <svg viewBox="0 0 12 12" aria-hidden="true"><path d="M2.4 0.6l1.8 2.4-1 1.2c.7 1.6 1.9 2.8 3.5 3.5l1.2-1 2.4 1.8-1 2.4C4.8 10.7 1.3 7.2.6 2.7z"/></svg>
        (718) 555-0143
      </li>
      <li>
        <svg viewBox="0 0 12 12" aria-hidden="true"><path d="M3 0h5l1 1v3H3zM1 5h10a1 1 0 0 1 1 1v5H0V6a1 1 0 0 1 1-1zm2 2v1h2V7zm4 0v1h2V7zM3 9v1h6V9z"/></svg>
        (888) 555-0176
      </li>
      <li>
        <svg viewBox="0 0 12 12" aria-hidden="true"><path d="M0 2h12v1L6 7 0 3zM0 4.3l6 4 6-4V10H0z"/></svg>
        mtkledger@quillpost.net
      </li>
      <li>
        <svg viewBox="0 0 12 12" aria-hidden="true"><path d="M5 3.5l1.6-1.6a2.3 2.3 0 0 1 3.3 3.3L8.3 6.8 7.4 5.9 9 4.3a1 1 0 0 0-1.4-1.4L6 4.4zM7 8.5L5.4 10.1a2.3 2.3 0 0 1-3.3-3.3L3.7 5.2l.9.9L3 7.7a1 1 0 0 0 1.4 1.4L6 7.6zM4 7.3l3.3-3.3.7.7-3.3 3.3z"/></svg>
        harborstonefiscalaidgroup.com
      </li>
    </ul>
  </section>
</main>
</body>
</html>
```